New Psychology Services looking for a Flyer Design

Flyer design is for a new psychology company "Tidal Lantern Psychologists" (logo provided) providing services to people across all ages. Desired theme colours for flyer is shades of soft greens and yellows, preferably in block/solid or abstract shapes or colours rather than pictures/little shapes (e.g. leaves). If picture included, perhaps an image of a person who is smiling or looking comfortable. Attached is sample of basic wording to be included in the flyer.

Contact number, logo and "curasure bulk billing available" must be in same page. Contact info should include "Locations across Southern & Eastern suburbs." Contact info and Logo and "Psychology Services" should also be the words that catch your eyes first on the flyer whether using layout/font or colour to create the effect.

Other information can be in different layout (either sides of the flyer; info in two columns as opposed to one etc.) as what we have now is very basic. Hopefully with some layout/spacing/colour work, it'll look fab. Thanks!

```html
<!DOCTYPE html>
<html lang="en">
<head>
<meta charset="utf-8">
<title>Tidal Lantern Psychologists – Psychology Services</title>
<link rel="stylesheet" href="https://fonts.googleapis.com/css2?family=Raleway:ital,wght@0,300;0,400;0,600;0,700;1,700&display=swap">
<style>
  :root {
    --green: #7dbb42;
    --green-soft: #a9d37c;
    --green-deep: #5f9a2c;
    --grey-text: #6e6e6e;
    --band: #dedede;
    --paper: #ffffff;
    --photo-light: #e8ebe4;
    --photo-mid: #b9c4c9;
    --photo-warm: #c79a78;
  }
  * { margin: 0; padding: 0; box-sizing: border-box; }
  html, body { width: 847px; height: 1200px; overflow: hidden; background: var(--paper); }
  body { font-family: "Raleway", Arial, sans-serif; color: var(--grey-text); }

  .flyer { position: relative; width: 847px; height: 1200px; overflow: hidden; background: var(--paper); }

  .hero-photo {
    position: absolute; left: 0; top: 0; width: 847px; height: 680px;
    background:
      radial-gradient(ellipse 260px 330px at 60px 300px, rgba(140,110,80,0.55), rgba(140,110,80,0) 70%),
      radial-gradient(ellipse 300px 220px at 560px 320px, rgba(90,130,190,0.45), rgba(90,130,190,0) 70%),
      radial-gradient(ellipse 220px 200px at 740px 360px, rgba(230,215,190,0.7), rgba(230,215,190,0) 70%),
      linear-gradient(180deg, var(--photo-light) 0%, var(--photo-mid) 60%, var(--photo-warm) 100%);
  }

  .hero-curve { position: absolute; left: 0; top: 500px; width: 847px; height: 180px; }

  .brand { position: absolute; top: 48px; left: 430px; width: 390px; text-align: center; }
  .brand-name {
    font-size: 40px; font-weight: 400; color: var(--green); letter-spacing: 1px; line-height: 1;
    text-transform: lowercase;
  }
  .brand-sub {
    margin-top: 6px; font-size: 14px; font-weight: 400; color: var(--green); letter-spacing: 4px;
    text-transform: uppercase;
  }

  .services { position: absolute; left: 62px; top: 612px; width: 380px; }
  .services-title {
    font-size: 31px; font-weight: 300; color: var(--green); letter-spacing: 0.5px; text-transform: uppercase;
    white-space: nowrap;
  }
  .title-rule { width: 363px; height: 3px; background: var(--green); margin: 8px 0 16px; }
  .services-intro {
    font-size: 14px; font-weight: 400; line-height: 1.5; text-transform: uppercase; letter-spacing: 0.3px;
    color: var(--grey-text);
  }

  .issue-columns { position: absolute; left: 62px; top: 805px; width: 760px; display: flex; gap: 22px; }
  .issue-column { width: 358px; }
  .issue-column + .issue-column { width: 370px; }
  .issue { margin-bottom: 24px; }
  .issue-name {
    font-size: 20px; font-weight: 700; font-style: italic; color: var(--green); text-transform: uppercase;
    letter-spacing: 0.5px; margin-bottom: 3px; line-height: 1.2;
  }
  .issue-list {
    font-size: 12.5px; font-weight: 400; line-height: 1.45; text-transform: uppercase; color: var(--grey-text);
    letter-spacing: 0.3px;
  }

  .contact-band {
    position: absolute; left: 0; bottom: 0; width: 847px; height: 92px;
    background: var(--green); color: var(--paper);
    display: flex; align-items: center; justify-content: space-between; padding: 0 62px;
  }
  .contact-phone { font-size: 32px; font-weight: 700; letter-spacing: 1px; display: flex; align-items: center; gap: 12px; }
  .contact-phone svg { width: 28px; height: 28px; }
  .contact-details { text-align: right; font-size: 14px; font-weight: 600; line-height: 1.5; text-transform: uppercase; letter-spacing: 0.5px; }
</style>
</head>
<body>
  <main class="flyer">
    <div class="hero-photo" role="img" aria-label="Photo of a smiling couple sitting on a sofa talking with a psychologist"></div>

    <svg class="hero-curve" viewBox="0 0 847 180" preserveAspectRatio="none" aria-hidden="true">
      <path d="M0 38 C 250 75, 550 125, 847 135 L 847 180 L 0 180 Z" fill="var(--band)"/>
      <path d="M0 58 C 250 97, 560 148, 847 158 L 847 180 L 0 180 Z" fill="var(--paper)"/>
    </svg>

    <header class="brand">
      <div class="brand-name">tidal lantern</div>
      <div class="brand-sub">Psychologists</div>
    </header>

    <section class="services">
      <h1 class="services-title">Psychology Services</h1>
      <div class="title-rule"></div>
      <p class="services-intro">Managing and finding out about mental health can often be difficult and confusing. Our psychologist see clients for a variety of issues including the following:</p>
    </section>

    <section class="issue-columns">
      <div class="issue-column">
        <div class="issue">
          <h2 class="issue-name">Mood Problems</h2>
          <p class="issue-list">(Mild to severe depression, bipolar disorder, anger management, emotional distress, etc.)</p>
        </div>
        <div class="issue">
          <h2 class="issue-name">Anxiety Issues</h2>
          <p class="issue-list">(Panic attacks, general anxiety, phobia, social anxiety, obsessive compulsive disorder, traumatic experiences, etc.)</p>
        </div>
        <div class="issue">
          <h2 class="issue-name">Grief</h2>
          <p class="issue-list">(Loss of loved one, relationship, home, work, furry friends, etc.)</p>
        </div>
      </div>
      <div class="issue-column">
        <div class="issue">
          <h2 class="issue-name">Adjustment Issues</h2>
          <p class="issue-list">(Work related stress, relationship difficulties, family conflict, unemployment, academic stress, bullying, behavioral issues, school refusal, change of school, migration, injuries/accidents, life stage transitions, etc.)</p>
        </div>
        <div class="issue">
          <h2 class="issue-name">Self-Esteem and Identity Issues</h2>
          <p class="issue-list">(Low confidence, poor social skills, gender identity issues, etc.)</p>
        </div>
      </div>
    </section>

    <footer class="contact-band">
      <div class="contact-phone">
        <svg viewBox="0 0 24 24" aria-hidden="true"><path fill="currentColor" d="M6.6 10.8a15.1 15.1 0 0 0 6.6 6.6l2.2-2.2a1 1 0 0 1 1-.25 11.4 11.4 0 0 0 3.6.57 1 1 0 0 1 1 1V20a1 1 0 0 1-1 1A17 17 0 0 1 3 4a1 1 0 0 1 1-1h3.5a1 1 0 0 1 1 1c0 1.25.2 2.45.57 3.57a1 1 0 0 1-.25 1z"/></svg>
        (03) 5550 1842
      </div>
      <div class="contact-details">
        <div>Locations across Southern &amp; Eastern suburbs</div>
        <div>curasure bulk billing available</div>
      </div>
    </footer>
  </main>
</body>
</html>
```